Stationary Design for Landscaping & Cleaning Business

Our landscaping and cleaning business need a stationary design, we would like separate designs for each business that match.
We want a simple yet bold design, using colours of our logos.
We are re designing our business so we need a more professional and modern look.
We don't want any extra words, just the basic contact details.
Name, address, phone number, email, abn and the usual customer details.
We would like to see examples for all stationary and both names.

Target Market(s)

No target market

Industry/Entity Type

Business

Font styles to use
Sans Serif

Colors
ffffff
000000

Requirements
Must have
• Business card, letterhead and envelope design.
Nice to have
• Lines and coloured areas
Should not have
• No extra pictures

```html
<!DOCTYPE html>
<html lang="en">
<head>
<meta charset="utf-8">
<title>Bright Sweep Crew – Business Card</title>
<link rel="stylesheet" href="https://fonts.googleapis.com/css2?family=Oswald:wght@300;400;500&display=swap">
<style>
  :root {
    --page: #f4f4f4;
    --lilac-light: #ecdff0;
    --lilac-deep: #c49fd2;
    --plum: #8a1c86;
    --plum-dark: #6e1670;
    --white: #ffffff;
    --charcoal: #48484b;
    --shadow: rgba(0, 0, 0, 0.18);
  }
  * { box-sizing: border-box; margin: 0; padding: 0; }
  html, body {
    width: 1200px;
    height: 798px;
    overflow: hidden;
    background: var(--page);
    font-family: "Oswald", sans-serif;
  }
  .canvas {
    width: 1200px;
    height: 798px;
    display: flex;
    align-items: center;
    justify-content: center;
    gap: 60px;
  }
  .card {
    width: 520px;
    height: 318px;
    position: relative;
    overflow: hidden;
    box-shadow: 0 6px 18px var(--shadow);
  }

  /* Front */
  .card-front {
    background: linear-gradient(110deg, var(--lilac-light) 0%, var(--lilac-deep) 100%);
  }
  .brand-name {
    color: var(--plum);
    font-weight: 400;
    letter-spacing: 0.5px;
    white-space: nowrap;
    line-height: 1;
  }
  .card-front .brand-name {
    position: absolute;
    left: 40px;
    top: 128px;
    font-size: 62px;
  }

  /* Back */
  .card-back { background: var(--white); }
  .back-header {
    height: 92px;
    background: linear-gradient(100deg, var(--lilac-light) 0%, var(--lilac-deep) 100%);
    position: relative;
  }
  .back-header .brand-name {
    position: absolute;
    left: 22px;
    bottom: 12px;
    font-size: 30px;
  }
  .contact {
    position: absolute;
    right: 22px;
    top: 16px;
    text-align right;
    text-align: right;
    color: var(--white);
  }
  .contact-phone { font-size: 24px; font-weight: 300; letter-spacing: 1px; line-height: 1.2; }
  .contact-web { font-size: 12px; font-weight: 300; letter-spacing: 1px; text-transform: uppercase; }

  .person {
    text-align: center;
    padding-top: 22px;
    padding-left: 70px;
  }
  .person-name {
    color: var(--plum-dark);
    font-size: 52px;
    font-weight: 500;
    line-height: 1;
    letter-spacing: 1px;
  }
  .person-title {
    color: var(--plum);
    font-size: 24px;
    font-weight: 400;
    letter-spacing: 1px;
    margin-top: 4px;
  }

  .address-bar {
    position: absolute;
    left: 0;
    right: 0;
    bottom: 0;
    height: 64px;
    background: var(--charcoal);
    display: flex;
    align-items: center;
    justify-content: space-around;
    padding: 0 16px;
    list-style: none;
  }
  .address-bar li {
    color: var(--white);
    font-size: 16px;
    font-weight: 400;
    letter-spacing: 1px;
  }
</style>
</head>
<body>
  <main class="canvas">
    <section class="card card-front" aria-label="Business card front">
      <h1 class="brand-name">Bright Sweep Crew</h1>
    </section>

    <section class="card card-back" aria-label="Business card back">
      <header class="back-header">
        <p class="brand-name">Bright Sweep Crew</p>
        <div class="contact">
          <p class="contact-phone">000-111-2222</p>
          <p class="contact-web">brightsweepcrew.com.au</p>
        </div>
      </header>
      <div class="person">
        <p class="person-name">YOUR NAME</p>
        <p class="person-title">JOB TITLE</p>
      </div>
      <ul class="address-bar">
        <li>STREET</li>
        <li>TOWN</li>
        <li>CITY</li>
        <li>STATE</li>
        <li>POST CODE</li>
      </ul>
    </section>
  </main>
</body>
</html>
```